MARLOWE THREADWORK WEB DESIGN PROJECT

We are a brand new company called "Marlowe Threadwork" which specialise in one-off Vintage Clothing. We would like somebody to design a web page which will be the sole income for our company. Our main aim is to have an easy searchable website which is user friendly. The key to the website is to target people who do not like the idea of op-shopping but love vintage clothes - this website will be the answer.
Updates

This website will need to be coded to work with Halvo Shopdesk - Please read this before you start. https://help.halvoshopdesk.example/articles/Public/How-do-I-create-custom-template-files-for-my-store

Hi everyone, Just want to make note that the this website is for young people. Just so people a clear I want modern young people dressed in Vintage clothes as this is that reality and what they would like to see. Not people dressed like they are going to a fancy dress party, i.e. dresses like it was that era. Thanks Rosalind

Coding

Coded - Design and coding required

```html
<!DOCTYPE html>
<html lang="en">
<head>
<meta charset="utf-8">
<title>Marlowe Threadwork – Vintage Dresses</title>
<link rel="stylesheet" href="https://fonts.googleapis.com/css2?family=Roboto+Condensed:wght@400;700&family=Open+Sans:wght@400;600&family=Kaushan+Script&display=swap">
<style>
:root{
  --pink:#f0507a;
  --ink:#2e2e2e;
  --charcoal:#333333;
  --header:#262626;
  --light:#f1f1f1;
  --line:#dcdcdc;
  --text:#444444;
  --white:#ffffff;
}
*{box-sizing:border-box;margin:0;padding:0}
html,body{width:1200px;height:2437px;overflow:hidden;background:var(--white)}
body{position:relative;font-family:"Roboto Condensed",Arial,sans-serif;color:var(--text)}
a{color:inherit;text-decoration:none}
ul{list-style:none}

.utility-bar{position:absolute;top:0;left:0;width:1200px;height:40px;display:flex;justify-content:flex-end;align-items:center;gap:36px;padding-right:40px;font-size:16px;color:var(--ink)}
.utility-bar span{display:flex;align-items:center;gap:10px}
.utility-bar svg{width:16px;height:16px}

.site-header{position:absolute;top:40px;left:0;width:1200px;height:124px;background:linear-gradient(90deg,#1e1e1e,#3a3a3a 55%,#222);color:var(--white)}
.brand{position:absolute;left:28px;top:26px}
.brand-name{font-weight:700;font-size:38px;color:var(--pink);letter-spacing:1px;line-height:1}
.brand-tagline{font-size:16px;margin-top:14px;letter-spacing:.5px}
.search{position:absolute;left:645px;top:26px;width:192px;height:32px;background:var(--white);display:flex}
.search input{flex:1;min-width:0;border:0;font:11px "Open Sans",sans-serif;padding-left:8px;color:#888;background:transparent}
.search button{width:32px;border:0;background:var(--pink);display:flex;align-items:center;justify-content:center}
.account{position:absolute;left:852px;top:26px;width:180px;height:32px;background:var(--white);color:var(--ink);font-size:13px;font-weight:700;display:flex;align-items:center;padding:0 12px;gap:10px}
.account .caret{margin-left:auto}
.header-links{position:absolute;left:1045px;top:26px;height:32px;display:flex;align-items:center;gap:14px;font-size:16px;font-weight:700}
.header-links i{width:1px;height:18px;background:#888}
.shipping-note{position:absolute;right:22px;top:80px;display:flex;align-items:center;gap:12px;font-size:16px;font-weight:700}

.gender-nav{position:absolute;top:166px;left:0;width:1200px;height:62px;display:flex;background:var(--pink)}
.gender-nav a{flex:none;display:flex;align-items:center;justify-content:center;gap:18px;font-size:34px;letter-spacing:1px;height:62px}
.gender-women{width:604px;color:var(--ink);border-right:4px solid var(--white)}
.gender-men{width:596px;color:var(--white)}
.gender-men span{border-bottom:3px solid var(--white);padding-bottom:2px}
.category-nav{position:absolute;top:228px;left:0;width:1200px;height:72px;background:var(--header);display:flex}
.category-nav a{display:flex;align-items:center;justify-content:center;color:var(--white);font-size:16px;border-right:2px solid #777;height:72px;white-space:nowrap}
.category-nav a.active{color:var(--pink)}
.category-nav a.current{border-bottom:3px solid var(--white)}

.breadcrumb{position:absolute;top:323px;left:20px;font-size:18px;color:var(--ink);display:flex;gap:12px}

.filters{position:absolute;top:370px;left:0;width:211px;height:1238px;border:1px solid var(--line);border-left:0;border-top:0}
.filter-group h3{height:32px;background:var(--charcoal);color:var(--white);font-size:16px;font-weight:400;padding:7px 18px;letter-spacing:.3px}
.filter-group ul{padding:10px 0 0 18px;font-family:"Open Sans",sans-serif;font-size:15px}
.filter-group li{height:28px;display:flex;align-items:center;gap:10px;color:var(--ink)}
.filter-group li.checked{color:var(--pink)}
.box{width:13px;height:13px;border:1px solid #bbb;background:var(--white);flex:none}
.filter-group .see-more{display:block;text-align:right;padding-right:24px;font-size:12px;color:#666;font-family:"Open Sans",sans-serif;border-bottom:1px solid var(--line);padding-bottom:4px}

.listing{position:absolute;top:366px;left:244px;width:900px}
.listing h1{font-size:21px;color:var(--pink);font-weight:700;letter-spacing:1px}
.listing p{margin-top:18px;font-family:"Open Sans",sans-serif;font-size:14.5px;line-height:22px;color:var(--ink);width:950px}
.product-grid{position:absolute;top:490px;left:246px;display:grid;grid-template-columns:242px 242px 242px;column-gap:66px 95px;column-gap:80px;row-gap:36px}
.product{height:347px;border:1px solid var(--line);background:var(--white);position:relative}
.product-photo{height:234px;position:relative;background:var(--light)}
.badge{position:absolute;top:0;right:0;width:30px;height:74px;background:#555;color:var(--white);font-size:13px;font-weight:700;display:flex;align-items:center;justify-content:center;writing-mode:vertical-rl;text-orientation:upright;letter-spacing:-2px}
.badge.sale{background:var(--pink)}
.price{position:absolute;right:0;bottom:0;width:50px;height:34px;background:#4a4a4a;color:var(--white);font-size:20px;display:flex;align-items:center;justify-content:center}
.price.sale{background:var(--pink)}
.product-name{text-align:center;font-size:18px;color:#555;margin-top:20px;letter-spacing:.3px}
.add-to-cart{position:absolute;left:38px;top:296px;width:168px;height:34px;display:flex;font-size:14px;color:var(--ink)}
.add-to-cart .cart-icon{width:48px;background:#cfcfcf;display:flex;align-items:center;justify-content:center}
.add-to-cart .label{flex:1;background:#b5b5b5;display:flex;align-items:center;justify-content:center}
.add-to-cart.active .cart-icon{background:var(--charcoal)}
.add-to-cart.active .label{background:var(--pink);color:var(--white)}

.pager-bar{position:absolute;top:1640px;left:0;width:1200px;height:42px;background:#f6f6f6;display:flex;align-items:center;font-family:"Open Sans",sans-serif;font-size:13px;color:#666}
.back-top{margin-left:16px;color:var(--pink);display:flex;align-items:center;gap:8px}
.pager{margin-left:auto;margin-right:70px;display:flex;gap:14px;align-items:center}
.pager .prev{color:var(--pink)}

.newsletter{position:absolute;top:1697px;left:0;width:1200px;height:276px;background:linear-gradient(90deg,#eadcd0,#f4ece4 45%,#f7f0ea)}
.newsletter-photo{position:absolute;left:0;top:0;width:560px;height:276px;background:linear-gradient(90deg,#6c5040 0%,#a7826a 35%,#d8c2b2 70%,rgba(244,236,228,0) 100%)}
.newsletter-copy{position:absolute;left:650px;top:24px;width:460px;text-align:center;color:#111}
.newsletter-copy .kicker{font-family:"Kaushan Script",cursive;font-size:36px}
.newsletter-copy h2{font-family:"Open Sans",sans-serif;font-weight:400;font-size:32px;margin-top:6px}
.email-field{width:325px;height:42px;margin:20px auto 0;background:var(--charcoal);color:var(--white);font-family:"Open Sans",sans-serif;font-size:15px;display:flex;align-items:center;justify-content:center}
.subscribe{width:118px;height:34px;margin:16px auto 0;background:var(--pink);color:var(--white);font-size:15px;font-weight:700;display:flex;align-items:center;justify-content:center;letter-spacing:.5px}

.social-bar{position:absolute;top:1973px;left:0;width:1200px;height:63px;background:var(--charcoal);display:flex;justify-content:space-around;align-items:center;padding:0 100px}
.social-bar a{display:flex;align-items:center;gap:10px;color:var(--white);font-size:17px}
.social-bar a i{width:30px;height:30px;border-radius:50%;background:var(--white)}

.site-footer{position:absolute;top:2036px;left:0;width:1200px;height:325px;background:var(--pink);color:var(--white);display:flex;padding:38px 0 0 60px}
.footer-col h4{font-size:23px;font-weight:400;margin-bottom:18px}
.footer-col li{font-family:"Open Sans",sans-serif;font-size:16px;height:33px;display:flex;gap:14px;align-items:center}
.footer-col li::before{content:"›";font-size:18px;margin-left:12px}
.col-about{width:408px}
.col-connect{width:390px}
.col-popular ul{display:grid;grid-template-columns:160px 80px;grid-auto-flow:column;grid-template-rows:repeat(5,33px)}
.col-popular li:nth-child(n+6)::before{content:none}

.bottom-bar{position:absolute;top:2361px;left:0;width:1200px;height:64px;display:flex;align-items:center;padding:0 66px;font-family:"Open Sans",sans-serif;font-weight:600;font-size:17px;color:#111}
.payments{margin-left:auto;display:flex;gap:28px;align-items:center;font-family:"Roboto Condensed",sans-serif;font-weight:700;font-size:20px;color:#333}
.payments span{display:flex;align-items:center;gap:8px}
.payments i{width:14px;height:14px;background:#333}
.bottom-strip{position:absolute;top:2425px;left:0;width:1200px;height:12px;background:var(--pink)}
</style>
</head>
<body>

<div class="utility-bar">
  <span><svg viewBox="0 0 16 16"><path d="M1 2h3l2 8h8l1-6H5" fill="none" stroke="#333" stroke-width="1.6"/><circle cx="7" cy="13.5" r="1.3" fill="#333"/><circle cx="13" cy="13.5" r="1.3" fill="#333"/></svg>View Cart</span>
  <span><svg viewBox="0 0 16 16"><path d="M8 14 2 8a3.5 3.5 0 0 1 6-4 3.5 3.5 0 0 1 6 4z" fill="none" stroke="#333" stroke-width="1.6"/></svg>Wish List</span>
  <span><svg viewBox="0 0 16 16"><circle cx="8" cy="8" r="6.5" fill="none" stroke="#333" stroke-width="1.6"/><path d="M6 6.2a2 2 0 1 1 2.5 2c-.5.2-.5.6-.5 1.4" fill="none" stroke="#333" stroke-width="1.5"/><circle cx="8" cy="12" r=".9" fill="#333"/></svg>Help</span>
</div>

<header class="site-header">
  <div class="brand">
    <div class="brand-name">Marlowe Threadwork</div>
    <div class="brand-tagline">Unique Vintage Fashion and Accessori</div>
  </div>
  <form class="search"><input value="Search one off vintage items"><button type="button"><svg width="16" height="16" viewBox="0 0 16 16"><circle cx="6.5" cy="6.5" r="4.5" fill="none" stroke="#fff" stroke-width="2"/><path d="M10 10l4.5 4.5" stroke="#fff" stroke-width="2"/></svg></button></form>
  <div class="account"><svg width="18" height="18" viewBox="0 0 18 18"><circle cx="9" cy="5" r="3.5" fill="#f0507a"/><path d="M2 17c0-5 3-7 7-7s7 2 7 7z" fill="#f0507a"/></svg>MY ACCOUNT<svg class="caret" width="10" height="6" viewBox="0 0 10 6"><path d="M0 0h10L5 6z" fill="#333"/></svg></div>
  <nav class="header-links"><a>STYLE TIPS</a><i></i><a>FAQ</a></nav>
  <div class="shipping-note"><svg width="34" height="22" viewBox="0 0 34 22"><rect x="0" y="2" width="20" height="14" fill="#f0507a"/><path d="M20 6h8l5 5v5H20z" fill="#f0507a"/><circle cx="7" cy="18" r="3" fill="#f0507a" stroke="#2b2b2b" stroke-width="1.5"/><circle cx="26" cy="18" r="3" fill="#f0507a" stroke="#2b2b2b" stroke-width="1.5"/></svg>ORDERS OVER $100 WILL RECEVIE FREE SHIPPING!</div>
</header>

<nav class="gender-nav">
  <a class="gender-women">WOMEN <svg width="30" height="40" viewBox="0 0 30 40"><path d="M11 1v7l-3 6 4 4L2 39h26L18 18l4-4-3-6V1" fill="#222"/></svg></a>
  <a class="gender-men"><span>MEN</span> <svg width="40" height="38" viewBox="0 0 40 38"><path d="M13 2l7 5 7-5 11 8-3 8-5-3v22H10V15l-5 3-3-8z" fill="none" stroke="#fff" stroke-width="2"/><path d="M20 7v30" stroke="#fff" stroke-width="1.5"/></svg></a>
</nav>
<nav class="category-nav">
  <a class="active" style="width:184px">VINTAGE CLOTHING</a>
  <a style="width:166px">VINTAGE SHOES</a>
  <a style="width:254px">OLD-FASHIONED ASSESSORIES</a>
  <a style="width:170px">VINTAGE CLOTHING</a>
  <a class="current" style="width:160px">VINTAGE SHOES</a>
  <a style="width:266px;border-right:0">OLD-FASHIONED ASSESSORIES</a>
</nav>

<div class="breadcrumb"><span>HOME</span><span>&gt;</span><span>WOMEN</span><span>&gt;</span><span>DRESS</span></div>

<aside class="filters">
  <section class="filter-group" style="height:168px"><h3>VINTAGE CLOTHES</h3><ul>
    <li class="checked"><svg class="box" viewBox="0 0 13 13"><path d="M2 6l3 3 6-7" fill="none" stroke="#f0507a" stroke-width="2"/></svg>Dresses &nbsp;&nbsp;(100)</li><li><i class="box"></i>Shirts &amp; T-Shirts &nbsp;(50)</li><li><i class="box"></i>Shorts &nbsp;&nbsp;(40)</li></ul><span class="see-more">See More</span></section>
  <section class="filter-group" style="height:150px"><h3>ERA</h3><ul>
    <li class="checked"><svg class="box" viewBox="0 0 13 13"><path d="M2 6l3 3 6-7" fill="none" stroke="#f0507a" stroke-width="2"/></svg>1950s</li><li><i class="box"></i>1960s</li><li><i class="box"></i>1970s</li></ul><span class="see-more">See More</span></section>
  <section class="filter-group" style="height:212px"><h3>SIZE</h3><ul>
    <li class="checked"><svg class="box" viewBox="0 0 13 13"><path d="M2 6l3 3 6-7" fill="none" stroke="#f0507a" stroke-width="2"/></svg>Six</li><li><i class="box"></i>Eight</li><li><i class="box"></i>Ten</li><li><i class="box"></i>Twelve</li><li><i class="box"></i>Fourteen</li></ul><span class="see-more">See More</span></section>
  <section class="filter-group" style="height:172px"><h3>COLOUR</h3><ul>
    <li class="checked"><svg class="box" viewBox="0 0 13 13"><path d="M2 6l3 3 6-7" fill="none" stroke="#f0507a" stroke-width="2"/></svg>Mixed</li><li><i class="box"></i>Black</li><li><i class="box"></i>White</li><li><i class="box"></i>Red</li></ul><span class="see-more">See More</span></section>
  <section class="filter-group" style="height:140px"><h3>PATTERN</h3><ul>
    <li class="checked"><svg class="box" viewBox="0 0 13 13"><path d="M2 6l3 3 6-7" fill="none" stroke="#f0507a" stroke-width="2"/></svg>Poke a dot</li><li><i class="box"></i>Floral</li><li><i class="box"></i>Stripes</li></ul><span class="see-more">See More</span></section>
  <section class="filter-group" style="height:144px"><h3>BRAND</h3><ul>
    <li class="checked"><svg class="box" viewBox="0 0 13 13"><path d="M2 6l3 3 6-7" fill="none" stroke="#f0507a" stroke-width="2"/></svg>xyz</li><li><i class="box"></i>xyz</li><li><i class="box"></i>xyz</li></ul><span class="see-more">See More</span></section>
  <section class="filter-group" style="height:252px"><h3>PRICE</h3><ul>
    <li class="checked"><svg class="box" viewBox="0 0 13 13"><path d="M2 6l3 3 6-7" fill="none" stroke="#f0507a" stroke-width="2"/></svg>$10-15</li><li><i class="box"></i>$15-$20</li><li><i class="box"></i>$20-$30</li><li><i class="box"></i>$30-$40</li><li><i class="box"></i>$40-$50</li><li><i class="box"></i>$50-$100</li><li><i class="box"></i>$100+</li></ul><span class="see-more" style="border:0">See More</span></section>
</aside>

<section class="listing">
  <h1>VINTAGE &nbsp;DRESSES</h1>
  <p>All our dresses are one off vintage pieces and are all pre loved. However all our clothes are condition and will look as though they are brand new. Be quick, as there is only one available per item and will disappear from the web once sold!</p>
</section>

<div class="product-grid">
  <article class="product"><div class="product-photo" role="img" aria-label="Coral and navy 1950s party dress on a dress form" style="background:radial-gradient(ellipse 60px 100px at 50% 55%,#2e3550,#e86f6a 60%,#f1f1f1 100%)"><span class="badge">NEW</span><span class="price">$25</span></div><div class="product-name">1950S &nbsp;PARTY DRESS</div><a class="add-to-cart"><span class="cart-icon"><svg width="18" height="14" viewBox="0 0 18 14"><path d="M0 1h3l2 8h9l2-6H4" fill="none" stroke="#333" stroke-width="1.6"/><circle cx="6" cy="12.5" r="1.3" fill="#333"/><circle cx="13" cy="12.5" r="1.3" fill="#333"/></svg></span><span class="label">ADD TO CART</span></a></article>
  <article class="product"><div class="product-photo" role="img" aria-label="Red sleeveless 1950s party dress on a dress form" style="background:radial-gradient(ellipse 60px 100px at 50% 55%,#d63a4c,#e06070 55%,#f1f1f1 100%)"><span class="badge sale">SALE</span><span class="price sale">$25</span></div><div class="product-name">1950S &nbsp;PARTY DRESS</div><a class="add-to-cart active"><span class="cart-icon"><svg width="18" height="14" viewBox="0 0 18 14"><path d="M0 1h3l2 8h9l2-6H4" fill="none" stroke="#fff" stroke-width="1.6"/><circle cx="6" cy="12.5" r="1.3" fill="#fff"/><circle cx="13" cy="12.5" r="1.3" fill="#fff"/></svg></span><span class="label">ADD TO CART</span></a></article>
  <article class="product"><div class="product-photo" role="img" aria-label="Coral wrap 1950s party dress on a dress form" style="background:radial-gradient(ellipse 55px 95px at 50% 55%,#ef5e62,#f07d7c 55%,#f1f1f1 100%)"><span class="badge">NEW</span><span class="price">$25</span></div><div class="product-name">1950S &nbsp;PARTY DRESS</div><a class="add-to-cart"><span class="cart-icon"><svg width="18" height="14" viewBox="0 0 18 14"><path d="M0 1h3l2 8h9l2-6H4" fill="none" stroke="#333" stroke-width="1.6"/><circle cx="6" cy="12.5" r="1.3" fill="#333"/><circle cx="13" cy="12.5" r="1.3" fill="#333"/></svg></span><span class="label">ADD TO CART</span></a></article>

  <article class="product"><div class="product-photo" role="img" aria-label="Orange vintage coat on a dress form" style="background:radial-gradient(ellipse 60px 100px at 50% 55%,#ee6a45,#f08a68 55%,#f1f1f1 100%)"><span class="badge">NEW</span><span class="price">$25</span></div><div class="product-name">1950S &nbsp;PARTY DRESS</div><a class="add-to-cart"><span class="cart-icon"><svg width="18" height="14" viewBox="0 0 18 14"><path d="M0 1h3l2 8h9l2-6H4" fill="none" stroke="#333" stroke-width="1.6"/><circle cx="6" cy="12.5" r="1.3" fill="#333"/><circle cx="13" cy="12.5" r="1.3" fill="#333"/></svg></span><span class="label">ADD TO CART</span></a></article>
  <article class="product"><div class="product-photo" role="img" aria-label="Red lace 1950s party dress on a dress form" style="background:radial-gradient(ellipse 60px 100px at 50% 55%,#e02f4a,#e65a6c 55%,#f1f1f1 100%)"><span class="badge">SALE</span><span class="price">$25</span></div><div class="product-name">1950S &nbsp;PARTY DRESS</div><a class="add-to-cart"><span class="cart-icon"><svg width="18" height="14" viewBox="0 0 18 14"><path d="M0 1h3l2 8h9l2-6H4" fill="none" stroke="#333" stroke-width="1.6"/><circle cx="6" cy="12.5" r="1.3" fill="#333"/><circle cx="13" cy="12.5" r="1.3" fill="#333"/></svg></span><span class="label">ADD TO CART</span></a></article>
  <article class="product"><div class="product-photo" role="img" aria-label="Pink-red shirt dress from the 1950s on a dress form" style="background:radial-gradient(ellipse 55px 100px at 50% 55%,#e03a58,#e8687e 55%,#f1f1f1 100%)"><span class="badge">NEW</span><span class="price">$25</span></div><div class="product-name">1950S &nbsp;PARTY DRESS</div><a class="add-to-cart"><span class="cart-icon"><svg width="18" height="14" viewBox="0 0 18 14"><path d="M0 1h3l2 8h9l2-6H4" fill="none" stroke="#333" stroke-width="1.6"/><circle cx="6" cy="12.5" r="1.3" fill="#333"/><circle cx="13" cy="12.5" r="1.3" fill="#333"/></svg></span><span class="label">ADD TO CART</span></a></article>

  <article class="product"><div class="product-photo" role="img" aria-label="Paisley print 1950s party dress on a dress form" style="background:radial-gradient(ellipse 60px 100px at 50% 55%,#8a3c36,#c27766 55%,#f1f1f1 100%)"><span class="badge">NEW</span><span class="price">$25</span></div><div class="product-name">1950S &nbsp;PARTY DRESS</div><a class="add-to-cart"><span class="cart-icon"><svg width="18" height="14" viewBox="0 0 18 14"><path d="M0 1h3l2 8h9l2-6H4" fill="none" stroke="#333" stroke-width="1.6"/><circle cx="6" cy="12.5" r="1.3" fill="#333"/><circle cx="13" cy="12.5" r="1.3" fill="#333"/></svg></span><span class="label">ADD TO CART</span></a></article>
  <article class="product"><div class="product-photo" role="img" aria-label="Red-orange fitted 1950s party dress on a dress form" style="background:radial-gradient(ellipse 55px 100px at 50% 55%,#e84a35,#ee7462 55%,#f1f1f1 100%)"><span class="badge">SALE</span><span class="price">$25</span></div><div class="product-name">1950S &nbsp;PARTY DRESS</div><a class="add-to-cart"><span class="cart-icon"><svg width="18" height="14" viewBox="0 0 18 14"><path d="M0 1h3l2 8h9l2-6H4" fill="none" stroke="#333" stroke-width="1.6"/><circle cx="6" cy="12.5" r="1.3" fill="#333"/><circle cx="13" cy="12.5" r="1.3" fill="#333"/></svg></span><span class="label">ADD TO CART</span></a></article>
  <article class="product"><div class="product-photo" role="img" aria-label="Teal long 1950s party dress on a dress form" style="background:radial-gradient(ellipse 50px 110px at 50% 55%,#0f6c6c,#4f9797 55%,#f1f1f1 100%)"><span class="badge">NEW</span><span class="price">$25</span></div><div class="product-name">1950S &nbsp;PARTY DRESS</div><a class="add-to-cart"><span class="cart-icon"><svg width="18" height="14" viewBox="0 0 18 14"><path d="M0 1h3l2 8h9l2-6H4" fill="none" stroke="#333" stroke-width="1.6"/><circle cx="6" cy="12.5" r="1.3" fill="#333"/><circle cx="13" cy="12.5" r="1.3" fill="#333"/></svg></span><span class="label">ADD TO CART</span></a></article>
</div>

<div class="pager-bar">
  <a class="back-top"><svg width="10" height="7" viewBox="0 0 10 7"><path d="M1 6l4-4 4 4" fill="none" stroke="#f0507a" stroke-width="1.6"/></svg>Back to Top</a>
  <div class="pager"><span>Showing 51 - 100 of 100 items</span><span>|</span><span>Show 100</span><span>|</span><span class="prev">‹ &nbsp;Prev</span><span>1</span><span>2</span><span>Next ›</span></div>
</div>

<section class="newsletter">
  <div class="newsletter-photo" role="img" aria-label="Young woman with long brown hair smiling beside a laptop"></div>
  <div class="newsletter-copy">
    <div class="kicker">Become part of our community</div>
    <h2>Sign up to our newsletter</h2>
    <div class="email-field">Email Address</div>
    <div class="subscribe">SUBSCRIBE</div>
  </div>
</section>

<nav class="social-bar">
  <a><i></i>Pinlorn</a>
  <a><i></i>Jotmere</a>
  <a><i></i>Friendvale</a>
  <a><i></i>Snaplark</a>
</nav>

<footer class="site-footer">
  <div class="footer-col col-about"><h4>Marlowe Threadwork</h4><ul><li>About Us</li><li>Terms of use</li><li>Privacy Policy</li><li>Press</li></ul></div>
  <div class="footer-col col-connect"><h4>Connect with Us</h4><ul><li>Contact us</li><li>My Account</li><li>Style Tips</li><li>FAQ</li><li>Shipping</li><li>Track your order</li><li>Size chart</li></ul></div>
  <div class="footer-col col-popular"><h4>Shop by Popular Categories</h4><ul><li>Men</li><li>Women</li><li>Accessories</li><li>Bags</li><li>Shoes</li><li>50s</li><li>6os</li><li>70s</li><li>80s</li><li>90s</li></ul></div>
</footer>

<div class="bottom-bar">
  <span>© &nbsp;Marlowe Threadwork. &nbsp;All Prices are in AUD.</span>
  <div class="payments"><span>Sealwick<i></i></span><span>Tillvane</span><span>Purselo</span><span>Cardoro</span><span>Duvanta</span></div>
</div>
<div class="bottom-strip"></div>

</body>
</html>
```